Book cover - Quiet Rooms, Open Doors

Book cover for Ebook (Pagelight) and wrap around print cover (Printvale) (back, front, and spine)

The book title (may slightly change by end of brief):
(MAIN TITLE) 'Quiet Rooms, Open Doors'
(SUB HEADING) 'A Week-by-Week Practical Workbook to Loosen Nervous Habits, Quieten Doubt and Build Steady Poise'
by Dr Owen Hartley

I would like a bold, stand out cover. Contemporary. I would like to avoid stereotypical images of people looking anxious or worried. I would like the design to be more uplifting and hopeful, rather than focusing on the negative aspect of anxiety, but avoiding cliched photos of people raising their hands in the air, smiling and jumping etc. The cover should appeal to both men and women.

Trim size of book cover (for PrintVale) is 5.25" x 8" back and front with a spine size of 0.477 inches

Reason: I have decided to extend the deadline by 1 more day, not because I am unhappy with the quality of the designs, but because a few designers have contacted me to explain they have had technical difficulties when submitting their files. Thanks everyone for the hard work and great designs.

Target Market(s)

Males and females (16+) who struggle with social anxiety and shyness

Industry/Entity Type

Social

Font styles to use
Serif

Requirements
Must have
• Bold cover that is modern and contemporary. For example, I like these covers:
• http://shrtlnk.example/k4Tq9Zb
• http://shrtlnk.example/m8Wv2Hn
• http://shrtlnk.example/p3Jx6Lr
• http://shrtlnk.example/t7Gd1Qe
• http://shrtlnk.example/v2Nk8Fy
• http://shrtlnk.example/w9Bh4Cs
• http://shrtlnk.example/z5Mf3Ud
Nice to have
• Open to abstract designs.
Should not have
• No stereotypical pictures of people who look anxious or worried. Avoid cliched photos of people raising their hands in the air, smiling and jumping etc.

```html
<!DOCTYPE html>
<html lang="en">
<head>
<meta charset="utf-8">
<title>Quiet Rooms, Open Doors — Book Cover</title>
<link rel="stylesheet" href="https://fonts.googleapis.com/css2?family=Dosis:wght@300;400&display=swap">
<style>
  :root {
    --paper: #ffffff;
    --ink: #3b3b3b;
    --ink-soft: #4a4a4a;
    --phone-dark: #3d3d3d;
    --screen: #f4f4f4;
    --skin: #f6c48e;
    --skin-deep: #eaa96a;
  }
  * { margin: 0; padding: 0; box-sizing: border-box; }
  html, body {
    width: 789px;
    height: 1200px;
    overflow: hidden;
    background: var(--paper);
  }
  .cover {
    position: relative;
    width: 789px;
    height: 1200px;
    background: var(--paper);
    color: var(--ink);
    font-family: "Dosis", "Helvetica Neue", Arial, sans-serif;
    text-align: center;
  }
  .cover__author {
    position: absolute;
    top: 26px;
    left: 0;
    width: 100%;
    font-size: 23px;
    font-weight: 400;
    letter-spacing: 0.5px;
    color: var(--ink-soft);
  }
  .cover__title {
    position: absolute;
    top: 74px;
    left: 0;
    width: 100%;
    font-size: 50px;
    line-height: 62px;
    font-weight: 300;
    letter-spacing: 0.5px;
  }
  .cover__artwork {
    position: absolute;
    left: 0;
    top: 310px;
    width: 610px;
    height: 735px;
    background: linear-gradient(160deg, var(--phone-dark) 0%, var(--phone-dark) 38%, var(--screen) 39%, var(--screen) 58%, var(--skin) 62%, var(--skin-deep) 100%);
    border-radius: 0 36px 36px 0;
  }
  .cover__subtitle {
    position: absolute;
    top: 1062px;
    left: 40px;
    width: 709px;
    font-size: 19px;
    line-height: 25px;
    font-weight: 400;
    color: var(--ink-soft);
  }
</style>
</head>
<body>
  <main class="cover">
    <p class="cover__author">Dr Owen Hartley</p>
    <h1 class="cover__title">Quiet Rooms,<br>Open Doors</h1>
    <div class="cover__artwork" role="img" aria-label="Flat illustration of a hand holding a smartphone showing an incoming call with a green answer button and a red decline button"></div>
    <p class="cover__subtitle">A Week-by-Week Practical Workbook to Loosen Nervous Habits, Quieten Doubt and Build Steady Poise</p>
  </main>
</body>
</html>
```